Dynamic Templates

Our company hosts web stores for our clients. They can set up as many as they wish on our platform, and select from the stock templates we provide. We are looking to increase the number of available stock templates.

Because our users can dynamically control many of the template elements - specifically colors - they have to be flexible and abide by certain rules. These rules are spelled out in the attached documents.

Here are links to two of our most used templates:
http://brivelta.tondashop.example/
http://quillorn.tondashop.example/

Templates need to have a landing page (what you see when first clicking one of the above links). There also needs to be a category page (what you see when clicking any category) and a product detail page (what you see when you arrive at an individual product, where there are various cart options like Buy Now or Request Info).

```html
<!DOCTYPE html>
<html lang="en">
<head>
<meta charset="utf-8">
<title>BrightCrate – Promotional Products</title>
<link rel="stylesheet" href="https://fonts.googleapis.com/css2?family=Arimo:wght@400&family=PT+Sans:wght@400&family=Roboto+Condensed:wght@400&display=swap">
<style>
  :root {
    --header-red: #d40b0b;
    --header-red-dark: #b80000;
    --header-edge: #5a0000;
    --brand-orange: #f07c00;
    --ink: #111111;
    --ink-soft: #222222;
    --page: #ffffff;
    --footer-grey: #b4b0b0;
    --footer-top: #d6d4d4;
    --divider: #ffffff;
    --frame: #333333;
  }
  * { box-sizing: border-box; margin: 0; padding: 0; }
  html, body { width: 1200px; height: 946px; overflow: hidden; background: var(--page); }
  body { position: relative; font-family: "Arimo", Arial, sans-serif; color: var(--ink); }

  .site-header {
    position: absolute; left: 0; top: 0; width: 1200px; height: 110px;
    background: linear-gradient(180deg, var(--header-red) 0%, var(--header-red-dark) 100%);
    border-bottom: 3px solid var(--header-edge);
    overflow: hidden;
  }
  .site-header .wave { position: absolute; left: 0; top: 0; }
  .brand { position: absolute; left: 101px; top: 30px; display: flex; align-items: center; gap: 12px; }
  .brand-dot { width: 47px; height: 47px; border-radius: 50%; background: var(--brand-orange); }
  .brand-name { font-family: "PT Sans", Arial, sans-serif; font-size: 24px; color: var(--brand-orange); }
  .header-contact {
    position: absolute; right: 101px; top: 42px; font-size: 17px; color: var(--ink-soft);
    border-bottom: 1px solid var(--ink-soft); line-height: 20px;
  }

  .featured { position: absolute; top: 135px; left: 102px; display: flex; gap: 20px; }
  .featured-item {
    width: 235px; height: 230px; border: 1px solid var(--frame); background: #fff; padding: 12px;
  }
  .featured-item .photo { width: 100%; height: 100%; }

  .intro { position: absolute; left: 103px; top: 386px; width: 720px; }
  .intro h1 { font-weight: 400; font-size: 28px; color: var(--brand-orange); line-height: 34px; margin-bottom: 14px; }
  .intro h2 { font-weight: 400; font-size: 21px; color: var(--brand-orange); line-height: 26px; margin: 4px 0 17px; }
  .intro p { font-size: 14px; line-height: 18.5px; margin-bottom: 18px; }

  .start-shopping {
    position: absolute; left: 954px; top: 411px; display: flex; align-items: center; gap: 2px;
    font-size: 15px; color: var(--ink); text-decoration: none;
  }

  .site-footer {
    position: absolute; left: 0; top: 652px; width: 1200px; height: 294px;
    background: var(--footer-grey); border-top: 4px solid var(--footer-top);
  }
  .footer-col {
    position: absolute; top: 20px; height: 230px;
    border-left: 1px solid var(--divider);
  }
  .footer-col h3 {
    font-family: "PT Sans", Arial, sans-serif; font-weight: 400; font-size: 23px; line-height: 28px; color: var(--ink);
  }
  .footer-list { list-style: none; font-family: "Roboto Condensed", "Arial Narrow", sans-serif; font-size: 17px; line-height: 24.6px; }
  .footer-list a { color: var(--ink); text-decoration: none; }
  .col-category { left: 101px; width: 512px; padding: 0 0 0 18px; }
  .col-category .lists { display: flex; margin-top: 6px; }
  .col-category .footer-list:nth-child(1) { width: 176px; }
  .col-category .footer-list:nth-child(2) { width: 161px; }
  .col-price { left: 613px; width: 242px; padding-left: 13px; }
  .col-price .footer-list { margin: 6px 0 0 64px; }
  .col-search { left: 855px; width: 245px; padding-left: 16px; border-right: 1px solid var(--divider); }
  .search-row { display: flex; align-items: center; gap: 10px; margin-top: 12px; }
  .search-row input { width: 179px; height: 32px; border: 1px solid #777; background: #fff; }
  .search-row span { font-family: "Roboto Condensed", sans-serif; font-size: 17px; }
  .col-search h3.contact { margin-top: 22px; }
  .contact-lines { font-family: "Roboto Condensed", sans-serif; font-size: 17px; line-height: 20px; margin-top: 10px; }
  .copyright { position: absolute; left: 0; width: 1200px; top: 258px; text-align: center; font-size: 15px; color: var(--ink); }
</style>
</head>
<body>
  <header class="site-header">
    <svg class="wave" width="1200" height="110" viewBox="0 0 1200 110" aria-hidden="true">
      <path d="M0 40 C 300 80, 700 10, 1200 55 L1200 110 L0 110 Z" fill="#c00404" opacity="0.55"/>
    </svg>
    <div class="brand">
      <span class="brand-dot"></span>
      <span class="brand-name">BrightCrate</span>
    </div>
    <div class="header-contact">Demo User . (555) 014-2290 . info@brightcrate.example</div>
  </header>

  <section class="featured">
    <div class="featured-item"><div class="photo" role="img" aria-label="Adventure kit tin with toy skier" style="background:radial-gradient(circle,#cfd9e6 0%,#a3492f 60%,#fff 100%)"></div></div>
    <div class="featured-item"><div class="photo" role="img" aria-label="Black cooler backpack filled with drinks and snacks" style="background:radial-gradient(circle,#3a3a3a 0%,#111 65%,#fff 100%)"></div></div>
    <div class="featured-item"><div class="photo" role="img" aria-label="Colourful puzzle pieces on a black round stand" style="background:linear-gradient(160deg,#fff 5%,#4fb3e0 30%,#f2c800 45%,#e03030 60%,#111 80%)"></div></div>
    <div class="featured-item"><div class="photo" role="img" aria-label="Grey and black picnic cooler tote with food" style="background:radial-gradient(circle,#9a9a9a 0%,#2a2a2a 60%,#fff 100%)"></div></div>
  </section>

  <main class="intro">
    <h1>Welcome To The Future of Promotional Products!</h1>
    <p>Gone are the days of searching through dog-eared catalogs or trying to make sense of complicated product websites.</p>
    <p>We do the work for you! We've taken only the very best and most current products and placed them in easy-to-use categories designed for your needs. Take a look at our selection - quality products at excellent prices.</p>
    <h2>Enjoy This Amazing New Resource</h2>
    <p>We know you don't have time to waste; so we've cut to the chase and made it simple! But keep in mind, we do have access to over a million products - so if you don't see what you're looking for or have a special theme or request, let us know - we'll find it!</p>
  </main>

  <a class="start-shopping" href="#">
    <svg width="26" height="26" viewBox="0 0 24 24" aria-hidden="true">
      <path d="M12 2 L14.9 8.6 L22 9.3 L16.6 14 L18.2 21 L12 17.3 L5.8 21 L7.4 14 L2 9.3 L9.1 8.6 Z" fill="#b8bde0" stroke="#7b80a8" stroke-width="0.8"/>
    </svg>
    Start shopping &gt;&gt;
  </a>

  <footer class="site-footer">
    <div class="footer-col col-category">
      <h3>Shop By Category</h3>
      <div class="lists">
        <ul class="footer-list">
          <li><a href="#">Apparel</a></li><li><a href="#">Business Supplies</a></li><li><a href="#">Company Outings</a></li><li><a href="#">Eco Friendly</a></li><li><a href="#">Food, Candy &amp; Drink</a></li><li><a href="#">Golf, Sports &amp; Outdoors</a></li><li><a href="#">Mugs &amp; Drinkware</a></li><li><a href="#">Tradeshows &amp; Events</a></li>
        </ul>
        <ul class="footer-list">
          <li><a href="#">Awards &amp; Recognition</a></li><li><a href="#">Caps &amp; Hats</a></li><li><a href="#">Corporate Gifts</a></li><li><a href="#">Electronics</a></li><li><a href="#">Games &amp; Novelties</a></li><li><a href="#">Healthcare &amp; Safety</a></li><li><a href="#">Notebooks &amp; Folios</a></li><li><a href="#">Writing Instruments</a></li>
        </ul>
        <ul class="footer-list">
          <li><a href="#">Bags &amp; Totes</a></li><li><a href="#">Clocks &amp; Watches</a></li><li><a href="#">Desktop &amp; Office</a></li><li><a href="#">Executive Gifts</a></li><li><a href="#">Gift Sets</a></li><li><a href="#">Keychains</a></li><li><a href="#">Tools &amp; Hardware</a></li>
        </ul>
      </div>
    </div>
    <div class="footer-col col-price">
      <h3>Shop By Price</h3>
      <ul class="footer-list">
        <li><a href="#">Under $5</a></li><li><a href="#">$5 - $10</a></li><li><a href="#">$10 - $20</a></li><li><a href="#">$20 - $50</a></li><li><a href="#">$50 - $100</a></li><li><a href="#">$100 - $200</a></li><li><a href="#">Over $200</a></li>
      </ul>
    </div>
    <div class="footer-col col-search">
      <h3>Quick Search</h3>
      <div class="search-row"><input type="text" aria-label="Search products"><span>Go</span></div>
      <h3 class="contact">Contact Us</h3>
      <div class="contact-lines">info@brightcrate.example<br>www.brightcrate.example</div>
    </div>
    <div class="copyright">Copyright © 2010 . BrightCrate.example V3 . All Rights Reserved.</div>
  </footer>
</body>
</html>
```